Webdesign for Dutch IT consultancy company

Make a Wordpress webdesign for a Dutch consultancy company

Briefing Velmora IT

Website for finding and connecting IT-professionals. Corebusiness is to find IT-professionals and to help them to follow their ambitions. We offer training, personal coaching and education trajects.

U can take www.Tralvique.nl as an example for the website.

Home page

U can take www.Tralvique.nl as an example.

There should be jobs on the home page. A block for short info about us and about what whe do and a trigger to contact us quickly.

Jobs Page

On this page should be the jobs that we offer for the professionals. There should be a search function on this page so u can easily find the job that you are looking for.

A call to action can be on this page too.

Also a little block with text for some information.

For professionals page

Block with information on top. Call to action. info about who we work for/with.

For Clients

Info about three different solutions

- Sourcing solutions
- Consultancy solutions
- Custom based traineeships

Request a qoute option

Traineeships page

Info about two different traineeships

- Linux traineeships
- Microsoft traineeships

Call to action/ subscribe for traineeships

About us page

We are Velmora IT

Our mission: Creating cooperations between young professionals and businesses who wanna work on a great future.

Our core values

Last news

Target Market(s)

Young professionals and businesses who need IT services

Industry/Entity Type

It Company

Coding

Coded - Design and coding required

Number of Pages Required

5+ page

Font styles to use
Other font styles liked:
• Calibri

Colors
ffffff
add136
6b449b

Requirements
Must have
• Home page, Jobs Page, Professionals page, Clients page, Traineeships page, About us Page
• Green and/or Purple layout. Job search option, subscribe option
Nice to have
• modern design

```html
<!DOCTYPE html>
<html lang="en">
<head>
<meta charset="utf-8">
<title>Velmora IT – Sourcing | Consultancy</title>
<link href="https://fonts.googleapis.com/css2?family=Open+Sans:wght@400;600;700&display=swap" rel="stylesheet">
<style>
:root{
  --purple:#6b449b;
  --purple-deep:#5a2d86;
  --green:#add136;
  --green-text:#8dbb1f;
  --blue:#2f5d9e;
  --ink:#222;
  --body:#555;
  --line:#dcdcdc;
  --page:#f6f6f6;
  --dark:#2a2a2a;
  --darker:#1e1e1e;
  --white:#fff;
}
*{margin:0;padding:0;box-sizing:border-box}
html,body{width:1200px;height:2601px;overflow:hidden}
body{position:relative;font-family:"Open Sans",Calibri,Arial,sans-serif;background:var(--page);color:var(--body)}
.abs{position:absolute}
a{text-decoration:none;color:inherit}

/* header */
.site-header{left:0;top:0;width:1200px;height:92px;background:var(--white)}
.brand{left:99px;top:24px;display:flex;align-items:center;gap:10px}
.brand-mark{width:34px;height:34px;border-radius:50%;background:var(--purple)}
.brand-name{font-size:32px;font-weight:700;color:var(--purple);letter-spacing:.5px;line-height:1}
.main-nav{right:98px;top:36px;display:flex;gap:39px;font-size:15px;color:#333}
.main-nav a.active{color:var(--green-text);border-bottom:2px solid var(--green);padding-bottom:6px}

/* hero */
.hero{left:0;top:92px;width:1200px;height:576px;background:linear-gradient(120deg,#6d655e 0%,#3f3a37 40%,#58524d 70%,#2b2826 100%)}
.hero-title{left:0;top:208px;width:1200px;text-align:center;color:var(--white);font-size:37px;font-weight:700;line-height:42px}
.hero-arrow{top:340px}
.hero-curve{left:0;top:600px}

/* sections */
.section-title{left:0;width:1200px;text-align:center;font-size:38px;font-weight:700;color:var(--ink);line-height:1}
.section-title.light{color:var(--white)}
.rule{left:560px;width:80px;height:3px;background:var(--green)}
.lead{left:200px;width:800px;text-align:center;font-size:14px;line-height:21px;color:#444}

/* jobs */
.job-col{width:288px}
.job-col h3{font-size:21px;font-weight:700;line-height:1;margin-bottom:17px}
.job-col.it h3{color:var(--purple)}
.job-col.net h3{color:var(--blue)}
.job-col.sup h3{color:var(--green-text)}
.job-list{list-style:none}
.job-list li{height:35px;margin-bottom:8px;background:var(--white);border:1px solid var(--line);font-size:13px;color:#333;display:flex;align-items:center;padding-left:10px;gap:7px}
.job-list svg{flex:none}
.view-all{display:block;margin-top:18px;font-size:14px;font-weight:700;text-decoration:underline}
.it .view-all{color:var(--purple)}
.net .view-all{color:var(--blue)}
.sup .view-all{color:var(--green-text)}

/* about */
.about{left:0;top:1224px;width:1200px;height:436px;background:linear-gradient(100deg,rgba(90,40,130,.95) 0%,rgba(107,68,155,.88) 55%,rgba(120,80,160,.8) 100%)}
.about-text{left:160px;width:880px;text-align:center;color:var(--white);font-size:14px;line-height:21px}
.btn-outline{border:2px solid var(--white);color:var(--white);display:flex;align-items:center;justify-content:center;letter-spacing:.5px}

/* what we do */
.service{width:330px;text-align:center}
.service-icon{width:116px;height:116px;border-radius:50%;margin:0 auto}
.service h4{margin-top:13px;font-size:22px;font-weight:600}
.service p{margin-top:9px;font-size:13.5px;line-height:21px;color:#555}

/* contact band */
.contact-band{left:0;top:2239px;width:1200px;height:300px;background:var(--dark)}
.site-footer{left:0;top:2539px;width:1200px;height:62px;background:var(--darker);color:#ddd;font-size:13px}
</style>
</head>
<body>

<header class="site-header abs">
  <div class="brand abs"><span class="brand-mark"></span><span class="brand-name">Velmora IT</span></div>
  <nav class="main-nav abs">
    <a class="active" href="#">Home</a><a href="#">Jobs</a><a href="#">Professionals</a><a href="#">Clients</a><a href="#">Traineeships</a><a href="#">About us</a><a href="#">Contact us</a>
  </nav>
</header>

<section class="hero abs" role="img" aria-label="Photo of young professionals working together at a laptop"></section>
<h1 class="hero-title abs">Creating cooperations between young professionals<br>and businesses who wanna work on a great future</h1>
<svg class="hero-arrow abs" style="left:30px" width="20" height="40" viewBox="0 0 20 40"><polyline points="17,3 3,20 17,37" fill="none" stroke="rgba(255,255,255,.6)" stroke-width="2"/></svg>
<svg class="hero-arrow abs" style="left:1142px" width="20" height="40" viewBox="0 0 20 40"><polyline points="3,3 17,20 3,37" fill="none" stroke="rgba(255,255,255,.6)" stroke-width="2"/></svg>
<svg class="hero-curve abs" width="1200" height="70" viewBox="0 0 1200 70"><path d="M0 70 Q600 -40 1200 70 Z" fill="var(--page)"/></svg>

<h2 class="section-title abs" style="top:680px">OUR JOBS</h2>
<div class="rule abs" style="top:724px"></div>
<p class="lead abs" style="top:754px">Quis autem vel eum iure reprehenderit qui in ea voluptate velit esse quam nihil molestiae consequatur, vel illum qui dolorem eum fugiat quo voluptas nulla pariatur</p>

<div class="job-col it abs" style="left:123px;top:849px">
  <h3>IT-PROFESSIONALS</h3>
  <ul class="job-list">
    <li><svg width="12" height="10" viewBox="0 0 12 10"><polyline points="1,5 4.5,8.5 11,1.5" fill="none" stroke="#6b449b" stroke-width="2.4"/></svg>Consequuntur Magni Dolores - Utrecht</li>
    <li><svg width="12" height="10" viewBox="0 0 12 10"><polyline points="1,5 4.5,8.5 11,1.5" fill="none" stroke="#6b449b" stroke-width="2.4"/></svg>Numquam Eius Modi - Den Bosch</li>
    <li><svg width="12" height="10" viewBox="0 0 12 10"><polyline points="1,5 4.5,8.5 11,1.5" fill="none" stroke="#6b449b" stroke-width="2.4"/></svg>Tempora Incidunt Ut - Amsterdam</li>
    <li><svg width="12" height="10" viewBox="0 0 12 10"><polyline points="1,5 4.5,8.5 11,1.5" fill="none" stroke="#6b449b" stroke-width="2.4"/></svg>Quis Nostrum Exercitat - Leiden</li>
    <li><svg width="12" height="10" viewBox="0 0 12 10"><polyline points="1,5 4.5,8.5 11,1.5" fill="none" stroke="#6b449b" stroke-width="2.4"/></svg>Vitae Dicta Sunt Explicabo - Rotterdam</li>
  </ul>
  <a class="view-all" href="#">View All Vacancies</a>
</div>

<div class="job-col net abs" style="left:456px;top:849px">
  <h3>NETWORKING JOBS</h3>
  <ul class="job-list">
    <li><svg width="12" height="10" viewBox="0 0 12 10"><polyline points="1,5 4.5,8.5 11,1.5" fill="none" stroke="#2f5d9e" stroke-width="2.4"/></svg>Quidem Rerum Facilis Est - Utrecht</li>
    <li><svg width="12" height="10" viewBox="0 0 12 10"><polyline points="1,5 4.5,8.5 11,1.5" fill="none" stroke="#2f5d9e" stroke-width="2.4"/></svg>Omnis Voluptas Assumenda - Den Bosch</li>
    <li><svg width="12" height="10" viewBox="0 0 12 10"><polyline points="1,5 4.5,8.5 11,1.5" fill="none" stroke="#2f5d9e" stroke-width="2.4"/></svg>Quibusdam Et Aut Officiis - Amsterdam</li>
    <li><svg width="12" height="10" viewBox="0 0 12 10"><polyline points="1,5 4.5,8.5 11,1.5" fill="none" stroke="#2f5d9e" stroke-width="2.4"/></svg>Rerum Necessitatibus Saepe - Leiden</li>
    <li><svg width="12" height="10" viewBox="0 0 12 10"><polyline points="1,5 4.5,8.5 11,1.5" fill="none" stroke="#2f5d9e" stroke-width="2.4"/></svg>Eveniet Ut Et Voluptates - Rotterdam</li>
  </ul>
  <a class="view-all" href="#">View All Vacancies</a>
</div>

<div class="job-col sup abs" style="left:791px;top:849px">
  <h3>IT-SUPPORTING</h3>
  <ul class="job-list">
    <li><svg width="12" height="10" viewBox="0 0 12 10"><polyline points="1,5 4.5,8.5 11,1.5" fill="none" stroke="#add136" stroke-width="2.4"/></svg>Tenetur a Sapiente Delectus - Utrecht</li>
    <li><svg width="12" height="10" viewBox="0 0 12 10"><polyline points="1,5 4.5,8.5 11,1.5" fill="none" stroke="#add136" stroke-width="2.4"/></svg>Numquam Eius Modi - Den Bosch</li>
    <li><svg width="12" height="10" viewBox="0 0 12 10"><polyline points="1,5 4.5,8.5 11,1.5" fill="none" stroke="#add136" stroke-width="2.4"/></svg>Cum Soluta Nobis Est&nbsp;&nbsp;- Amsterdam</li>
    <li><svg width="12" height="10" viewBox="0 0 12 10"><polyline points="1,5 4.5,8.5 11,1.5" fill="none" stroke="#add136" stroke-width="2.4"/></svg>Maxime Placeat Facere Possimus - Leiden</li>
    <li><svg width="12" height="10" viewBox="0 0 12 10"><polyline points="1,5 4.5,8.5 11,1.5" fill="none" stroke="#add136" stroke-width="2.4"/></svg>Necessitatibus Saepe Eveniet - Rotterdam</li>
  </ul>
  <a class="view-all" href="#">View All Vacancies</a>
</div>

<section class="about abs" role="img" aria-label="Photo of a team in a meeting behind a purple overlay"></section>
<h2 class="section-title light abs" style="top:1277px">ABOUT US</h2>
<div class="rule abs" style="top:1321px;background:var(--white)"></div>
<p class="about-text abs" style="top:1342px">Sed ut perspiciatis unde omnis iste natus error sit voluptatem accusantium doloremque laudantium, totam rem aperiam, eaque ipsa quae ab illo inventore veritatis et quasi architecto beatae vitae dicta sunt explicabo. Nemo enim ipsam voluptatem quia voluptas sit aspernatur aut odit aut fugit, sed quia consequuntur magni dolores eos qui ratione voluptatem sequi nesciunt. Neque porro quisquam est, qui dolorem ipsum quia dolor sit amet, consectetur, adipisci velit, sed quia non numquam eius modi tempora incidunt ut labore et dolore magnam aliquam quaerat voluptatem.</p>
<p class="about-text abs" style="top:1446px">But I must explain to you how all this mistaken idea of denouncing pleasure and praising pain was born and I will give you a complete account of the system, and expound the actual teachings of the great explorer of the truth, the master-builder of human happiness.</p>
<a class="btn-outline abs" href="#" style="left:506px;top:1524px;width:186px;height:46px;font-size:18px">LEARN MORE</a>

<h2 class="section-title abs" style="top:1733px">WHAT WE DO</h2>
<div class="rule abs" style="top:1777px"></div>
<p class="lead abs" style="top:1811px;left:130px;width:940px;line-height:26px">At vero eos et accusamus et iusto odio dignissimos ducimus qui blanditiis praesentium voluptatum deleniti atque corrupti quos dolores et quas molestias excepturi sint occaecati cupiditate non provident.</p>

<div class="service abs" style="left:74px;top:1917px">
  <div class="service-icon" style="background:#444"></div>
  <h4 style="color:#333">Training</h4>
  <p>Quis autem vel eum iure reprehenderit qui in ea voluptate velit esse quam nihil molestiae consequatur</p>
</div>
<div class="service abs" style="left:435px;top:1917px">
  <div class="service-icon" style="background:var(--green)"></div>
  <h4 style="color:var(--green-text)">Personal Coaching</h4>
  <p>Quis autem vel eum iure reprehenderit qui in ea voluptate velit esse quam nihil molestiae consequatur</p>
</div>
<div class="service abs" style="left:794px;top:1917px">
  <div class="service-icon" style="background:var(--purple-deep)"></div>
  <h4 style="color:var(--purple-deep)">Education Trajects</h4>
  <p>Quis autem vel eum iure reprehenderit qui in ea voluptate velit esse quam nihil molestiae consequatur</p>
</div>

<section class="contact-band abs"></section>
<h2 class="section-title light abs" style="top:2309px">KNOWING MORE?</h2>
<div class="rule abs" style="top:2353px"></div>
<a class="btn-outline abs" href="#" style="left:515px;top:2407px;width:168px;height:46px;font-size:14px;font-weight:600">CONTACT US</a>

<footer class="site-footer abs">
  <p class="abs" style="left:99px;top:21px">© 2017 Velmora IT.&nbsp; All right reserved . Term of Use</p>
  <span class="abs" style="left:1024px;top:23px;width:14px;height:14px;border-radius:50%;background:#ddd"></span>
  <span class="abs" style="left:1052px;top:23px;width:14px;height:14px;border-radius:50%;background:#ddd"></span>
  <span class="abs" style="left:1085px;top:23px;width:14px;height:14px;border-radius:50%;background:#ddd"></span>
</footer>

</body>
</html>
```